Packaging design for health, nutrition, essential oils, herbals, vitamins and product lines. We want an upscale design that is aligned with nature. Must add a tree graphic into the design because our products are forest or tree products.

We need boxes, bottles, tags, labels for herbs, herbal formulas, vitamin bottles,

This is the text that will be on the packaging.

Larkmoor Botanical Therapeutics (bold this)
-- insert eclectic tree graphic ---
Aligned With Nature
Est. Aspen, Colorado

The colors of our brand are
Platinum, White, Silver, Chrome, Clear Glass
The Graphic we need is an eclectic or cool forest tree preferably pine trees or christmas trees but we are also open to an eclectic tree graphic

We also need to see a tree graphic in the branding packaging
We are opened to adding some green to the packaging as well

Our products that we need the packaging for are
Herbs and Herbal Formulas
Beverages
Fragrances
Aromatherapy
Essential Oils
Nutritional Products
Vitamins, Supplements and Minerals

It is very important to provide us with a luxury brand that compliments our firm, Larkmoor Physicians.
This is a new division of our firm that delivers all
100% ALL NATURAL PLANT BASED PRODUCTS and INDIGENOUS MEDICINES

I love the idea of having
platinum or shiny silver contrast against minimalist white and or glass and a must have is to add green (forest or herbal green color) and a tree graphic

Again : Our products are all forest and plant based

We also will have the same designer create a web page for the commerce store after this project

Project Deadline Extended Reason: Need to see more design options to be sure. Thus far only one designer has anything worthy of our brand. Added Saturday, May 7, 2016

Luxury Consumers, Plant Based Medicine and Natural Healing Consumers, Herbs and Herbal Formula Consumers, Health Conscious Consumers, Nature or Environmental Products Consumers, High Networth Consumers

Health Product

• Colors : Platinum, Silver, Chrome, White and A Tree or Plant Leaves Graphic, Preferably a Forest Tree
• Maintain same font as our LarkmoorPhysicians.example logo brand
• No other colors besides white, platinum, silver, chrome or forest or tree green

```html
<!DOCTYPE html>
<html lang="en">
<head>
<meta charset="utf-8">
<title>Larkmoor Botanical Therapeutics — Rosemary Essential Oil Label</title>
<link rel="stylesheet" href="https://fonts.googleapis.com/css2?family=Josefin+Sans:wght@600;700&family=Cormorant+SC:wght@500;600&display=swap">
<style>
  :root {
    --backdrop: #e9e9e9;
    --label-silver: #a6a7a6;
    --label-silver-light: #b3b4b3;
    --ink: #161816;
    --ink-soft: #2e312e;
    --rule: #6f716f;
    --forest-mist: #8c918c;
    --forest-mid: #4d544e;
    --forest-deep: #0f1210;
    --band: #080908;
    --platinum-text: #e6e7e6;
  }
  * { box-sizing: border-box; margin: 0; padding: 0; }
  html, body {
    width: 1200px;
    height: 1200px;
    overflow: hidden;
    background: var(--backdrop);
  }
  .canvas {
    position: relative;
    width: 1200px;
    height: 1200px;
  }
  .label {
    position: absolute;
    left: 250px;
    top: 85px;
    width: 700px;
    height: 1030px;
    background: linear-gradient(180deg, var(--label-silver-light) 0%, var(--label-silver) 100%);
    overflow: hidden;
    text-align: center;
    color: var(--ink);
  }
  .brand-mark {
    position: absolute;
    left: 50%;
    top: 44px;
    width: 62px;
    height: 62px;
    margin-left: -31px;
    background: var(--platinum-text);
    border-radius: 4px;
  }
  .brand-name {
    position: absolute;
    top: 128px;
    left: 0;
    right: 0;
    font-family: "Josefin Sans", sans-serif;
    font-weight: 700;
    font-size: 20px;
    letter-spacing: 2px;
    text-transform: uppercase;
    color: var(--ink-soft);
  }
  .brand-origin {
    position: absolute;
    top: 160px;
    left: 0;
    right: 0;
    font-family: "Cormorant SC", serif;
    font-weight: 600;
    font-size: 15px;
    letter-spacing: 1px;
    color: var(--ink-soft);
  }
  .divider {
    position: absolute;
    left: 90px;
    right: 90px;
    height: 0;
    border-top: 3px dashed var(--rule);
    opacity: 0.8;
  }
  .divider--top { top: 305px; }
  .divider--bottom { top: 468px; }
  .product-name {
    position: absolute;
    top: 345px;
    left: 0;
    right: 0;
    font-family: "Josefin Sans", sans-serif;
    font-weight: 700;
    font-size: 50px;
    letter-spacing: 3px;
    text-transform: uppercase;
    color: var(--ink);
  }
  .product-name .percent { font-size: 40px; letter-spacing: 0; }
  .product-type {
    position: absolute;
    top: 420px;
    left: 0;
    right: 0;
    font-family: "Josefin Sans", sans-serif;
    font-weight: 700;
    font-size: 30px;
    letter-spacing: 3px;
    text-transform: uppercase;
    color: var(--ink-soft);
  }
  .forest {
    position: absolute;
    left: 0;
    right: 0;
    top: 570px;
    bottom: 0;
    background: linear-gradient(180deg,
      var(--label-silver) 0%,
      var(--forest-mist) 22%,
      var(--forest-mid) 48%,
      var(--forest-deep) 78%,
      var(--band) 100%);
  }
  .tagline-band {
    position: absolute;
    left: 0;
    right: 0;
    bottom: 0;
    height: 86px;
    background: var(--band);
  }
  .tagline {
    position: absolute;
    left: 0;
    right: 0;
    bottom: 28px;
    font-family: "Cormorant SC", serif;
    font-weight: 600;
    font-size: 28px;
    letter-spacing: 3px;
    color: var(--platinum-text);
  }
</style>
</head>
<body>
  <main class="canvas">
    <section class="label">
      <div class="brand-mark" aria-hidden="true"></div>
      <h1 class="brand-name">Larkmoor Botanical Therapeutics</h1>
      <p class="brand-origin">Est. Aspen, Colorado</p>

      <div class="divider divider--top" aria-hidden="true"></div>
      <h2 class="product-name"><span class="percent">100%</span> Rosemary</h2>
      <p class="product-type">Essential Oil</p>
      <div class="divider divider--bottom" aria-hidden="true"></div>

      <div class="forest" role="img" aria-label="Pine forest silhouette fading from misty silver to black"></div>
      <div class="tagline-band" aria-hidden="true"></div>
      <p class="tagline">Aligned with Nature</p>
    </section>
  </main>
</body>
</html>
```